Herbal Tincture Product Packaging

Rebrand herbal product labels for use on 2 oz tincture bottles - current packaging attached. (no box needed). Bottles are frosted glass Boston rounds 2 oz with silver cap dropper. logo options attached. 3 products/varieties: Harbor, Lantern, Meadow - would really also like a visual icon to represent product variety at a glance, in addition to name.
Please see guidelines below:
Label Material:
Base- polyester, BOPP, or other non-vinyl synthetics Lamination- matte or gloss Backing- white or kraft, no transparent
Spooling:
Rewind direction #4, 3” core, not more that 1200 per roll, not less than 500 per roll Please include 5-10% overage (ex. if you have 500 units on order, please print 525-550 labels).
Sizing:
2oz. ABR- >/= 2” H x 4.5” W
Suggested guidelines review:
https://www.krvl.org/files/Document%20Library/KRVL%20Guidance%20Documents/Packaging%20and%20Labeling/KRVL%20Guidance_Herbal%20Supplements%20Labeling%20Guide%20(Revised%202021).pdf
Target Market(s)
Health Conscious age 24+
Industry/Entity Type
holistic health care
Colors
Look and feel

```html
<!DOCTYPE html>
<html lang="en">
<head>
<meta charset="utf-8">
<title>Wrenfield Apothecary – Tincture Labels</title>
<link href="https://fonts.googleapis.com/css2?family=Josefin+Sans:wght@300;400&family=Lora:wght@400;700&display=swap" rel="stylesheet">
<style>
  :root {
    --page-bg: #eeeeec;
    --label-bg: #f3f3f2;
    --label-edge: #dcdcda;
    --ink: #2b2b2b;
    --ink-soft: #4a4a4a;
    --harbor-light: #b3d066;
    --harbor-dark: #76a01c;
    --lantern-light: #93acd9;
    --lantern-dark: #2a519e;
    --meadow-light: #ebc67c;
    --meadow-dark: #c68b1c;
  }
  * { box-sizing: border-box; margin: 0; padding: 0; }
  html, body {
    width: 1200px; height: 1200px; overflow: hidden;
    background: var(--page-bg);
  }
  .label-set {
    position: relative; width: 1200px; height: 1200px;
  }
  .label {
    position: absolute; top: 392px;
    width: 318px; height: 418px;
    background: var(--label-bg);
    border: 1px solid var(--label-edge);
    border-radius: 3px;
    overflow: hidden;
  }
  .label--harbor  { left: 73px;  --light: var(--harbor-light);  --dark: var(--harbor-dark); }
  .label--lantern { left: 441px; --light: var(--lantern-light); --dark: var(--lantern-dark); }
  .label--meadow  { left: 809px; --light: var(--meadow-light);  --dark: var(--meadow-dark); }

  .brand-mark {
    position: absolute; left: 50%; top: 20px; transform: translateX(-50%);
    width: 100px; height: 100px; border-radius: 50%;
    background: var(--light);
  }
  .brand-name {
    position: absolute; left: 0; right: 0; top: 128px;
    text-align: center;
    font-family: "Lora", serif; font-weight: 400;
    font-size: 22px; letter-spacing: 3px;
    color: var(--ink);
    line-height: 1.25;
  }
  .brand-rule {
    position: absolute; left: 88px; width: 142px; top: 189px;
    height: 2px; background: var(--ink);
  }
  .product-name {
    position: absolute; left: 0; right: 0; top: 220px;
    text-align: center;
    font-family: "Lora", serif; font-weight: 700;
    font-size: 48px; letter-spacing: 0.5px; line-height: 1;
    background: linear-gradient(90deg, var(--light), var(--dark));
    -webkit-background-clip: text; background-clip: text;
    color: transparent;
  }
  .tagline {
    position: absolute; right: 160px; top: 294px;
    text-align: right;
    font-family: "Josefin Sans", sans-serif; font-weight: 300;
    font-size: 17px; letter-spacing: 1.2px; line-height: 21px;
    color: var(--ink-soft);
  }
  .divider {
    position: absolute; left: 169px; top: 292px;
    width: 2px; height: 68px; background: var(--ink);
  }
  .variety-icon {
    position: absolute; left: 186px; top: 282px;
    width: 82px; height: 86px; border-radius: 6px;
    background: linear-gradient(160deg, var(--light), #cfcfcf);
  }
  .info-band {
    position: absolute; left: 0; right: 0; top: 376px; height: 38px;
    background: linear-gradient(90deg, var(--light), var(--dark));
    display: flex; align-items: center; justify-content: center;
    font-family: "Josefin Sans", sans-serif; font-weight: 300;
    font-size: 17px; color: #fbfbf8; letter-spacing: 0.2px;
  }
</style>
</head>
<body>
  <main class="label-set">
    <section class="label label--harbor">
      <div class="brand-mark"></div>
      <div class="brand-name">WRENFIELD<br>APOTHECARY</div>
      <div class="brand-rule"></div>
      <h2 class="product-name">HARBOR</h2>
      <p class="tagline">TEAS<br>TONICS<br>TINCTURES</p>
      <div class="divider"></div>
      <div class="variety-icon" role="img" aria-label="Harbor variety icon: figure in meditation with sprouting leaves"></div>
      <div class="info-band">HERBAL SUPPORT · 2 oz 60 ml</div>
    </section>

    <section class="label label--lantern">
      <div class="brand-mark"></div>
      <div class="brand-name">WRENFIELD<br>APOTHECARY</div>
      <div class="brand-rule"></div>
      <h2 class="product-name">LANTERN</h2>
      <p class="tagline">EVERYDAY<br>HERBALS<br>TINCTURES</p>
      <div class="divider"></div>
      <div class="variety-icon" role="img" aria-label="Lantern variety icon: leaping figure with a water swirl"></div>
      <div class="info-band">HERBAL SUPPORT · 2 oz 60 ml</div>
    </section>

    <section class="label label--meadow">
      <div class="brand-mark"></div>
      <div class="brand-name">WRENFIELD<br>APOTHECARY</div>
      <div class="brand-rule"></div>
      <h2 class="product-name">MEADOW</h2>
      <p class="tagline">EVERYDAY<br>HERBALS<br>TINCTURES</p>
      <div class="divider"></div>
      <div class="variety-icon" role="img" aria-label="Meadow variety icon: figure with raised arms beneath golden leaves"></div>
      <div class="info-band">HERBAL SUPPORT · 2 oz 60 ml</div>
    </section>
  </main>
</body>
</html>
```